Real Estate - Large Sign Design

I am looking for a fresh new look for our leasing signs that will be showcase in front of commercial buildings available for lease. The sign dimension can be either 8'x4' or 4'x8'. They must exemplify our brand (see attachments) and be very visible by people driving by at high speeds.
They must include the following:
- Our logo (vector attached)
- Office Space Available
- 555-018-3274
- Nell Ruby
- Carl Ivey
- www.vantorile.com
Please let me know if you have any questions.
Target Market(s)
Drivers in high traffic areas, walking crowds
Industry/Entity Type
Real Estate
Requirements
Must have
- They must include the following:
- - Our logo (vector attached)
- - Office Space Available
- - 555-018-3274
- - Nell Ruby
- - Carl Ivey
- - www.vantorile.com
Should not have
- Should not be busy or hard to read.

```html
<!DOCTYPE html>
<html lang="en">
<head>
<meta charset="utf-8">
<title>Office Space Available – Leasing Sign</title>
<link rel="stylesheet" href="https://fonts.googleapis.com/css2?family=Roboto+Condensed:ital,wght@0,400;0,700;0,900;1,400&display=swap">
<style>
  :root {
    --backdrop: #e9ecee;
    --sign-white: #ffffff;
    --ink: #0d0d0d;
    --brand-green: #2f8a57;
    --green-light: #8cc63f;
    --green-mid: #3fae49;
    --green-deep: #1f8a4c;
    --green-dark: #2e6a4f;
    --name-grey: #2f3d37;
    --logo-text: #ffffff;
  }
  * { margin: 0; padding: 0; box-sizing: border-box; }
  html, body {
    width: 1200px;
    height: 791px;
    overflow: hidden;
    background: var(--backdrop);
    font-family: "Roboto Condensed", "Arial Narrow", sans-serif;
  }
  .leasing-sign {
    position: absolute;
    left: 50px;
    top: 120px;
    width: 1100px;
    height: 550px;
    background: var(--sign-white);
    overflow: hidden;
    box-shadow: 0 6px 24px rgba(0,0,0,0.18);
  }
  .sign-shapes {
    position: absolute;
    inset: 0;
    width: 100%;
    height: 100%;
  }
  .headline {
    position: absolute;
    left: 34px;
    top: 30px;
    text-transform: uppercase;
    line-height: 0.86;
  }
  .headline-main {
    display: block;
    font-weight: 900;
    font-size: 168px;
    letter-spacing: -3px;
    color: var(--ink);
  }
  .headline-sub {
    display: block;
    font-weight: 900;
    font-size: 118px;
    letter-spacing: 1px;
    color: var(--brand-green);
    margin-top: 8px;
  }
  .contact {
    position: absolute;
    left: 38px;
    top: 338px;
    line-height: 1;
  }
  .contact-names {
    font-weight: 700;
    font-size: 28px;
    color: var(--name-grey);
    text-transform: uppercase;
    letter-spacing: 0.5px;
  }
  .contact-divider {
    margin: 0 10px;
    color: var(--brand-green);
  }
  .contact-phone {
    font-weight: 700;
    font-size: 58px;
    color: var(--ink);
    letter-spacing: -1px;
    margin-top: 6px;
  }
  .contact-web {
    font-style: italic;
    font-weight: 400;
    font-size: 24px;
    color: var(--ink);
    margin-top: 4px;
  }
  .company-name {
    position: absolute;
    right: 34px;
    bottom: 40px;
    font-weight: 400;
    font-size: 32px;
    line-height: 1.05;
    color: var(--logo-text);
    text-transform: uppercase;
    letter-spacing: 1px;
  }
</style>
</head>
<body>
  <main class="leasing-sign">
    <svg class="sign-shapes" viewBox="0 0 1100 550" preserveAspectRatio="none" aria-hidden="true">
      <defs>
        <linearGradient id="band-gradient" x1="0" y1="1" x2="1" y2="0.6">
          <stop offset="0" stop-color="var(--green-light)"/>
          <stop offset="0.55" stop-color="var(--green-mid)"/>
          <stop offset="1" stop-color="var(--green-deep)"/>
        </linearGradient>
        <linearGradient id="corner-gradient" x1="0" y1="0" x2="0" y2="1">
          <stop offset="0" stop-color="var(--green-dark)"/>
          <stop offset="1" stop-color="var(--green-deep)"/>
        </linearGradient>
      </defs>
      <polygon class="accent-band" points="0,530 1100,330 1100,550 0,550" fill="url(#band-gradient)"/>
      <polygon class="accent-corner" points="1085,0 1100,0 1100,550 800,550" fill="url(#corner-gradient)"/>
    </svg>

    <h1 class="headline">
      <span class="headline-main">Office Space</span>
      <span class="headline-sub">Available</span>
    </h1>

    <section class="contact">
      <p class="contact-names">Carl Ivey<span class="contact-divider">|</span>Nell Ruby</p>
      <p class="contact-phone">555-018-3274</p>
      <p class="contact-web">www.vantorile.com</p>
    </section>

    <p class="company-name">Harwell<br>Property<br>Company</p>
  </main>
</body>
</html>
```